Castlereagh Yard Works L.L.C.
Repair Maintenance Improvement
Professional
Patrick Dunleavy
do not want address
pat@castlereaghyardworks.example
Thank You!
The finest compliment I could ever receive is a referral from my friends and customers.

```html
<!DOCTYPE html>
<html lang="en">
<head>
<meta charset="utf-8">
<title>Castlereagh Yard Works L.L.C. – Business Cards</title>
<link href="https://fonts.googleapis.com/css2?family=PT+Sans:wght@400;700&display=swap" rel="stylesheet">
<style>
  :root {
    --page: #ffffff;
    --frame: #9a9a9a;
    --card: #ffffff;
    --card-edge: #8c8c8c;
    --brand: #3e5a4d;
    --brand-dark: #2b4237;
    --band-top: #4a6457;
    --band-bottom: #2a3f35;
    --ink: #222222;
    --name: #4b5f55;
    --light: #ffffff;
  }
  * { box-sizing: border-box; margin: 0; padding: 0; }
  html, body { width: 1200px; height: 758px; overflow: hidden; background: var(--page); }
  body { font-family: "PT Sans", Arial, sans-serif; color: var(--ink); }

  .sheet {
    position: relative; width: 1200px; height: 758px;
    border: 3px solid var(--frame); background: var(--page);
  }
  .card {
    position: absolute; background: var(--card);
    border: 2px solid var(--card-edge); border-radius: 24px;
    box-shadow: 4px 6px 10px rgba(0,0,0,0.28);
    overflow: hidden;
  }
  .card--front  { left: 36px;  top: 26px;  width: 554px; height: 341px; }
  .card--banded { left: 36px;  top: 391px; width: 554px; height: 322px; }
  .card--back   { left: 622px; top: 234px; width: 548px; height: 326px; }

  .brand { position: absolute; width: 330px; }
  .brand__name {
    display: flex; align-items: flex-start; gap: 10px;
    font-weight: 700; font-size: 31px; line-height: 1.05; color: var(--brand);
  }
  .brand__mark { flex: none; width: 14px; height: 14px; margin-top: 9px; background: var(--brand); }
  .brand__tagline {
    margin-top: 8px; margin-left: 24px;
    font-weight: 700; font-size: 12.5px; letter-spacing: 1.6px; color: var(--brand-dark);
    text-transform: uppercase;
  }
  .card--front .brand  { left: 34px; top: 48px; }
  .card--banded .brand { left: 34px; top: 30px; }
  .card--back .brand   { left: 118px; top: 44px; width: 320px; }
  .card--back .brand__tagline { text-align: center; margin-left: 0; }

  .holder { position: absolute; font-size: 26px; line-height: 1; color: var(--name); }
  .card--front .holder  { left: 40px; top: 258px; }
  .card--banded .holder { left: 40px; top: 253px; color: var(--light); }

  .contact { position: absolute; list-style: none; font-size: 14px; line-height: 1; }
  .contact li { display: flex; align-items: center; gap: 10px; height: 26px; }
  .contact svg { width: 13px; height: 13px; flex: none; }
  .card--front .contact  { left: 250px; top: 244px; color: var(--ink); }
  .card--banded .contact { left: 250px; top: 250px; color: var(--light); }

  .band {
    position: absolute; left: 0; right: 0; top: 205px; bottom: 0;
    background: linear-gradient(180deg, var(--band-top), var(--band-bottom));
  }

  .thanks { position: absolute; left: 0; right: 0; top: 212px; text-align: center; font-size: 15px; line-height: 1.45; }
  .thanks__title { font-weight: 700; }
</style>
</head>
<body>
<main class="sheet">

  <section class="card card--front" aria-label="Business card front">
    <div class="brand">
      <div class="brand__name"><span class="brand__mark"></span><span>Castlereagh Yard Works L.L.C.</span></div>
      <div class="brand__tagline">Repair • Maintenance • Improvement</div>
    </div>
    <p class="holder">Patrick Dunleavy</p>
    <ul class="contact">
      <li><svg viewBox="0 0 14 14"><rect x="0.5" y="2.5" width="13" height="9" fill="currentColor"/><path d="M1 3 L7 8 L13 3" stroke="#fff" stroke-width="1.2" fill="none"/></svg>pat@castlereaghyardworks.example</li>
      <li><svg viewBox="0 0 14 14"><rect x="3" y="0.5" width="8" height="13" rx="1.5" fill="currentColor"/><rect x="4.5" y="2" width="5" height="8" fill="#fff"/></svg>555.014.7968</li>
    </ul>
  </section>

  <section class="card card--banded" aria-label="Business card front, banded version">
    <div class="brand">
      <div class="brand__name"><span class="brand__mark"></span><span>Castlereagh Yard Works L.L.C.</span></div>
      <div class="brand__tagline">Repair • Maintenance • Improvement</div>
    </div>
    <div class="band"></div>
    <p class="holder">Patrick Dunleavy</p>
    <ul class="contact">
      <li><svg viewBox="0 0 14 14"><rect x="0.5" y="2.5" width="13" height="9" fill="currentColor"/><path d="M1 3 L7 8 L13 3" stroke="#2f463b" stroke-width="1.2" fill="none"/></svg>pat@castlereaghyardworks.example</li>
      <li><svg viewBox="0 0 14 14"><rect x="3" y="0.5" width="8" height="13" rx="1.5" fill="currentColor"/><rect x="4.5" y="2" width="5" height="8" fill="#2f463b"/></svg>555.014.7968</li>
    </ul>
  </section>

  <section class="card card--back" aria-label="Business card back">
    <div class="brand">
      <div class="brand__name"><span class="brand__mark"></span><span>Castlereagh Yard Works L.L.C.</span></div>
      <div class="brand__tagline">Repair • Maintenance • Improvement</div>
    </div>
    <div class="thanks">
      <p class="thanks__title">Thank You!</p>
      <p>The finest compliment I could ever<br>receive is a referral from my friends and customers.</p>
    </div>
  </section>

</main>
</body>
</html>
```